Custom Manufacturing Company square space website design

I own a custom manufacturing company that uses precision cutting technology to manufacture project components over a couple industries. We have an industrial CNC router and state of the art edge bander and cut a lot of cabinetry components for cabinet shops, builders, closet companies, ect. We offer design and assembly for any cabinetry or can build cabinets to spec. We also cut components for other industries out of wood, plastics, acryclics, ect. We offer design engineering services, product development protype services. we have a 3D printer farm. We want our communicate trust, dependability, and the value we place on client relationships.

We essentially want a credibility website. Landing page and drops downs for services we offer, capabilites, about us, contact

```html
<!DOCTYPE html>
<html lang="en">
<head>
<meta charset="utf-8">
<title>Northgate CNC</title>
<link href="https://fonts.googleapis.com/css2?family=Oswald:wght@400;500;600&family=Nunito+Sans:wght@400;600;700&display=swap" rel="stylesheet">
<style>
:root{
  --ink:#161616;
  --dark:#111111;
  --panel:#2d2d2d;
  --tile-dim:#2a2a2a;
  --grey:#efefef;
  --line:#d9d9d9;
  --white:#ffffff;
  --muted:#6d6d6d;
  --head:'Oswald',sans-serif;
  --body:'Nunito Sans',sans-serif;
}
*{box-sizing:border-box;margin:0;padding:0}
html,body{width:1200px;height:4289px;overflow:hidden}
body{position:relative;background:var(--grey);font-family:var(--body);color:var(--ink)}
.abs{position:absolute}
.h2{font-family:var(--head);font-weight:500;font-size:31px;text-transform:uppercase;text-align:center;left:0;width:1200px;letter-spacing:.2px}
.btn{position:absolute;font-family:var(--head);font-weight:500;font-size:15px;display:flex;align-items:center;justify-content:center;text-transform:uppercase}
.btn-dark{background:#2f2f2f;color:var(--white)}
.btn-light{background:var(--white);color:var(--ink)}
.photo{position:absolute}

/* header */
.site-header{left:0;top:0;width:1200px;height:143px;background:var(--white)}
.brand{display:flex;align-items:center;gap:10px}
.brand-mark{width:30px;height:30px;border:2px solid currentColor}
.brand-name{font-family:var(--body);font-weight:700;font-size:18px;letter-spacing:2px}
.topbar{font-family:var(--head);font-size:12px;top:32px;display:flex;align-items:center;gap:6px}
.search{left:910px;top:26px;width:130px;height:26px;border-bottom:1px solid #bbb;font-size:11px;color:#aaa;padding:6px 0 0 4px}
.nav-rule{left:441px;top:70px;width:600px;height:1px;background:var(--line)}
.nav{top:100px;font-family:var(--head);font-size:13px;color:#222}
.quote-btn{left:930px;top:92px;width:109px;height:36px;border:1.5px solid #222;font-family:var(--head);font-weight:500;font-size:14px;display:flex;align-items:center;justify-content:center}

/* hero */
.hero-copy h1{font-family:var(--head);font-weight:500;font-size:36px;line-height:44px;color:var(--white)}
.hero-copy p{font-size:19px;line-height:29px;color:#eee;margin-top:10px}

/* cards */
.card{position:absolute;background:var(--white);box-shadow:0 2px 10px rgba(0,0,0,.12)}
.service-text{font-family:var(--head);font-size:13px;line-height:22px;text-align:center;text-transform:uppercase;width:240px}
.project-cap{position:absolute;left:0;bottom:0;width:256px;height:93px;background:#262626;color:var(--white);font-family:var(--head);font-size:13px;line-height:19px;padding:17px 0 0 17px;text-transform:uppercase;clip-path:polygon(0 0,100% 0,100% 100%,0 100%)}
.arrow-box{position:absolute;width:40px;height:40px;background:#111;display:flex;align-items:center;justify-content:center}
.arrow-box.light{background:#1f1f1f}

/* about */
.about p{font-size:14px;line-height:28px;color:#e6e6e6}
.stat-num{font-family:var(--head);font-weight:600;font-size:33px}
.stat-label{font-size:13px;color:#333}

/* process */
.step-circle{position:absolute;width:156px;height:156px;border-radius:50%;background:var(--white);border:1px solid #ddd;box-shadow:0 2px 8px rgba(0,0,0,.07);display:flex;align-items:center;justify-content:center}
.step-label{position:absolute;width:200px;text-align:center;font-family:var(--head);font-weight:500;font-size:16px;line-height:20px;text-transform:uppercase}

/* capabilities */
.cap-tile{position:absolute;top:2999px;height:196px;background:var(--white);display:flex;flex-direction:column;align-items:center;justify-content:flex-end;padding-bottom:40px;gap:22px;font-family:var(--head);font-weight:500;font-size:16px;text-transform:uppercase}
.cap-tile.dim{background:var(--tile-dim);color:#555}

/* contact */
.field-label{position:absolute;font-size:11px;color:#999}
.field-line{position:absolute;height:1px;background:#bdbdbd}
.contact-item{position:absolute;left:230px;color:var(--white);font-size:15px;display:flex;gap:12px;align-items:flex-start;line-height:20px}

/* footer */
.foot-nav{position:absolute;top:4166px;font-size:14px;color:#ddd}
.social{position:absolute;top:4245px;width:25px;height:25px;border:1px solid #ccc}
</style>
</head>
<body>

<!-- header -->
<header class="abs site-header">
  <div class="abs brand" style="left:163px;top:50px;color:#1a1a1a">
    <span class="brand-mark"></span><span class="brand-name">NORTHGATE CNC</span>
  </div>
  <div class="abs topbar" style="left:598px">
    <svg width="13" height="13" viewBox="0 0 24 24" fill="none" stroke="#222" stroke-width="2"><path d="M5 3h4l2 5-3 2a11 11 0 0 0 6 6l2-3 5 2v4a2 2 0 0 1-2 2A17 17 0 0 1 3 5a2 2 0 0 1 2-2z"/></svg>(123) 456-7890
  </div>
  <div class="abs topbar" style="left:728px">
    <svg width="13" height="11" viewBox="0 0 24 18" fill="none" stroke="#222" stroke-width="2"><rect x="1" y="1" width="22" height="16"/><path d="M1 1l11 9 11-9"/></svg>info@northgatecnc.com
  </div>
  <div class="abs search">Search...</div>
  <svg class="abs" style="left:1025px;top:33px" width="12" height="12" viewBox="0 0 24 24" fill="none" stroke="#111" stroke-width="3"><circle cx="10" cy="10" r="7"/><path d="M15 15l7 7"/></svg>
  <div class="abs nav-rule"></div>
  <span class="abs nav" style="left:440px">Home</span>
  <span class="abs nav" style="left:506px">About Us</span>
  <span class="abs nav" style="left:592px">Services ⌄</span>
  <span class="abs nav" style="left:690px">Capabilities</span>
  <span class="abs nav" style="left:788px">CONTACT US</span>
  <div class="abs quote-btn">Request A Quote</div>
</header>

<!-- hero -->
<section>
  <div class="photo" role="img" aria-label="Machinist operating a CNC drill press with coolant spray" style="left:0;top:143px;width:1200px;height:508px;background:linear-gradient(100deg,#1e2328 0%,#33393f 45%,#5d6166 62%,#2c3136 80%,#1a1d20 100%)"></div>
  <div class="abs hero-copy" style="left:163px;top:266px;width:520px">
    <h1>Looking For A Reliable Supplier For CNC Machining, Production Machining Services?</h1>
    <p>Providing high precision short run machining services for local industry in Western New York.</p>
  </div>
  <div class="btn" style="left:161px;top:473px;width:166px;height:48px;border:1.5px solid #fff;color:#fff;font-size:16px;text-transform:none">Request A Quote</div>
</section>

<!-- what we do -->
<section>
  <h2 class="abs h2" style="top:710px">What We Do</h2>
  <div class="card" style="left:151px;top:764px;width:899px;height:324px"></div>
  <div class="photo" role="img" aria-label="Cabinet design drawing on a computer monitor" style="left:200px;top:809px;width:230px;height:161px;background:linear-gradient(160deg,#d9dadb,#8e9296)"></div>
  <div class="photo" role="img" aria-label="Worker cutting material on a CNC router" style="left:484px;top:809px;width:230px;height:161px;background:linear-gradient(160deg,#4b5a63,#1f2a30)"></div>
  <div class="photo" role="img" aria-label="Engineering prototype being machined" style="left:770px;top:809px;width:230px;height:161px;background:linear-gradient(160deg,#3e4e7a,#6b6f78)"></div>
  <div class="abs service-text" style="left:195px;top:990px">We offer design and assembly for any cabinetry or can build cabinets to specifications.</div>
  <div class="abs service-text" style="left:479px;top:990px">We also cut components for other industries out of wood, plastics, acrylics, etc.</div>
  <div class="abs service-text" style="left:765px;top:990px">We offer design engineering services, product development protype services.</div>
</section>

<!-- recent projects -->
<section>
  <h2 class="abs h2" style="top:1133px">Recent Projects</h2>
  <div class="arrow-box" style="left:121px;top:1310px"><svg width="18" height="12" viewBox="0 0 18 12" fill="none" stroke="#fff" stroke-width="1.6"><path d="M17 6H1M6 1L1 6l5 5"/></svg></div>
  <div class="arrow-box" style="left:1038px;top:1310px"><svg width="18" height="12" viewBox="0 0 18 12" fill="none" stroke="#fff" stroke-width="1.6"><path d="M1 6h16M12 1l5 5-5 5"/></svg></div>

  <div class="abs" style="left:196px;top:1211px;width:256px;height:263px">
    <div class="photo" role="img" aria-label="Angle grinder throwing sparks in a workshop" style="left:0;top:0;width:256px;height:263px;background:linear-gradient(150deg,#3a3634,#7a5a3a 55%,#2a2a2a)"></div>
    <div class="project-cap">Lorem ipsum dolor sit amet,<br>consectetur adipiscing elit.<br>Etiam suscipit lorem.</div>
    <svg class="abs" style="left:190px;top:170px" width="66" height="93" viewBox="0 0 66 93"><path d="M30 0H66V93H0z" fill="#1a1a1a"/><path d="M32 47h18M45 42l5 5-5 5" stroke="#fff" stroke-width="1.6" fill="none"/></svg>
  </div>
  <div class="abs" style="left:473px;top:1211px;width:256px;height:263px">
    <div class="photo" role="img" aria-label="CNC spindle cutting with a tablet held nearby" style="left:0;top:0;width:256px;height:263px;background:linear-gradient(150deg,#5b5f63,#b8bcbf 55%,#3b3f44)"></div>
    <div class="project-cap">Lorem ipsum dolor sit amet,<br>consectetur adipiscing elit.<br>Etiam suscipit lorem.</div>
    <svg class="abs" style="left:190px;top:170px" width="66" height="93" viewBox="0 0 66 93"><path d="M30 0H66V93H0z" fill="#1a1a1a"/><path d="M32 47h18M45 42l5 5-5 5" stroke="#fff" stroke-width="1.6" fill="none"/></svg>
  </div>
  <div class="abs" style="left:749px;top:1211px;width:256px;height:263px">
    <div class="photo" role="img" aria-label="Welder working at a bench with bright arc light" style="left:0;top:0;width:256px;height:263px;background:linear-gradient(150deg,#4a4f4a,#6d7a8c 55%,#2b2d30)"></div>
    <div class="project-cap">Lorem ipsum dolor sit amet,<br>consectetur adipiscing elit.<br>Etiam suscipit lorem.</div>
    <svg class="abs" style="left:190px;top:170px" width="66" height="93" viewBox="0 0 66 93"><path d="M30 0H66V93H0z" fill="#1a1a1a"/><path d="M32 47h18M45 42l5 5-5 5" stroke="#fff" stroke-width="1.6" fill="none"/></svg>
  </div>
  <div class="btn btn-dark" style="left:533px;top:1513px;width:134px;height:40px">View All</div>
</section>

<!-- about -->
<section class="about">
  <div class="abs" style="left:0;top:1564px;width:1200px;height:583px;background:var(--dark)"></div>
  <svg class="abs" style="left:0;top:1564px" width="1200" height="100" viewBox="0 0 1200 100">
    <polygon points="0,0 530,82 670,82 1200,0" fill="#3a3a3a"/>
    <polygon points="0,0 530,72 670,72 1200,0" fill="var(--grey)"/>
  </svg>
  <h2 class="abs" style="left:163px;top:1693px;font-family:var(--head);font-weight:500;font-size:36px;color:#fff">ABOUT US</h2>
  <p class="abs" style="left:163px;top:1762px;width:430px">Lorem ipsum dolor sit amet, consectetur adipiscing elit. Etiam suscipit lorem eget ligula tincidunt pharetra. Sed aliquam lacus et dolor tempus mollis. Etiam luctus, metus eget lobortis porttitor, arcu orci bibendum dolor, ut accumsan lacus nibh et nisi. Curabitur et pharetra orci. Sed vulputate erat risus. Sed lobortis nunc eleifend ornare ultrices. Mauris eget justo nisi. Nulla ultrices commodo orci ac vulputate. Nunc at leo quis elit tincidunt placerat. Nunc lacinia rutrum varius.</p>
  <div class="btn btn-light" style="left:161px;top:2017px;width:135px;height:41px">Read More</div>
  <div class="photo" role="img" aria-label="Engineer in a hard hat operating an industrial CNC control panel" style="left:644px;top:1694px;width:355px;height:369px;background:linear-gradient(135deg,#8b9096,#c9ccd0 40%,#2c3550 70%,#1c2236)"></div>

  <svg class="abs" style="left:0;top:2020px" width="1200" height="130" viewBox="0 0 1200 130">
    <polygon points="0,127 600,7 1200,127 1200,130 0,130" fill="var(--grey)"/>
    <polygon points="151,73 600,7 1050,73 1050,130 151,130" fill="#fff"/>
  </svg>
  <div class="abs" style="left:151px;top:2093px;width:899px;height:193px;background:#fff;box-shadow:0 4px 10px rgba(0,0,0,.1)"></div>

  <div class="abs" style="left:196px;top:2125px">
    <svg width="44" height="40" viewBox="0 0 44 40" fill="none" stroke="#333" stroke-width="2"><rect x="2" y="10" width="40" height="28" rx="2"/><path d="M15 10V4h14v6M2 20h40M20 17h4v6h-4z"/></svg>
    <div class="stat-num">20+</div><div class="stat-label">Years of Experience</div>
  </div>
  <div class="abs" style="left:411px;top:2125px">
    <svg width="44" height="40" viewBox="0 0 44 40" fill="none" stroke="#333" stroke-width="2"><path d="M6 2v38M6 4h30v18H6M6 9h30M6 14h30M2 40h10"/></svg>
    <div class="stat-num">100%</div><div class="stat-label">Made in America</div>
  </div>
  <div class="abs" style="left:626px;top:2125px">
    <svg width="44" height="40" viewBox="0 0 44 40" fill="none" stroke="#333" stroke-width="2"><circle cx="22" cy="20" r="18"/><path d="M4 20h36M22 2c-8 10-8 26 0 36M22 2c8 10 8 26 0 36"/></svg>
    <div class="stat-num">GLOBAL</div><div class="stat-label">Servicimg &nbsp;the Globe</div>
  </div>
  <div class="abs" style="left:840px;top:2125px">
    <svg width="44" height="40" viewBox="0 0 44 40" fill="none" stroke="#333" stroke-width="2"><circle cx="16" cy="14" r="11"/><circle cx="16" cy="14" r="5"/><path d="M10 24l-3 12 9-4 9 4-3-12"/></svg>
    <div style="width:66px;height:28px;background:#2a2a2a;margin:4px 0 6px"></div>
    <div class="stat-label">Industry Standatrds Met</div>
  </div>
</section>

<!-- process -->
<section>
  <h2 class="abs h2" style="top:2378px">Our Process</h2>
  <div class="step-circle" style="left:202px;top:2461px"><svg width="66" height="66" viewBox="0 0 64 64" fill="none" stroke="#222" stroke-width="2.2"><path d="M10 34a22 22 0 0 1 44 0zM6 34h52v6H6zM26 14v12M38 14v12M16 40c2 12 30 12 32 0"/></svg></div>
  <div class="step-circle" style="left:416px;top:2461px"><svg width="66" height="66" viewBox="0 0 64 64" fill="none" stroke="#222" stroke-width="2.2"><path d="M32 6l26 14-26 14L6 20zM6 30l26 14 26-14M6 40l26 14 26-14"/></svg></div>
  <div class="step-circle" style="left:629px;top:2461px"><svg width="66" height="66" viewBox="0 0 64 64" fill="none" stroke="#222" stroke-width="2.2"><path d="M8 8h48M24 8v10h16V8M28 18l4 8 4-8M32 32v8M10 48h44v6H10z"/></svg></div>
  <div class="step-circle" style="left:842px;top:2461px"><svg width="70" height="66" viewBox="0 0 68 64" fill="none" stroke="#222" stroke-width="2.2"><path d="M14 18h30v26H14zM44 26h10l8 9v9H44zM4 26h8M2 34h10"/><circle cx="22" cy="46" r="5"/><circle cx="52" cy="46" r="5"/></svg></div>
  <svg class="abs" style="left:368px;top:2530px" width="38" height="18" viewBox="0 0 38 18" fill="none" stroke="#777" stroke-width="3"><path d="M2 2l7 7-7 7M13 2l7 7-7 7M24 2l7 7-7 7"/></svg>
  <svg class="abs" style="left:580px;top:2530px" width="38" height="18" viewBox="0 0 38 18" fill="none" stroke="#777" stroke-width="3"><path d="M2 2l7 7-7 7M13 2l7 7-7 7M24 2l7 7-7 7"/></svg>
  <svg class="abs" style="left:793px;top:2530px" width="38" height="18" viewBox="0 0 38 18" fill="none" stroke="#777" stroke-width="3"><path d="M2 2l7 7-7 7M13 2l7 7-7 7M24 2l7 7-7 7"/></svg>
  <div class="step-label" style="left:180px;top:2638px">Application<br>Engineering</div>
  <div class="step-label" style="left:394px;top:2638px">Material<br>Selection</div>
  <div class="step-label" style="left:607px;top:2638px">Part<br>Fabrication</div>
  <div class="step-label" style="left:820px;top:2638px">Delivery</div>
  <div class="btn btn-dark" style="left:533px;top:2712px;width:134px;height:42px">Get Started</div>
</section>

<!-- capabilities -->
<section>
  <div class="abs" style="left:0;top:2771px;width:1200px;height:540px;background:var(--dark)"></div>
  <svg class="abs" style="left:0;top:2771px" width="1200" height="90" viewBox="0 0 1200 90">
    <polygon points="0,0 530,74 670,74 1200,0" fill="var(--grey)"/>
  </svg>
  <h2 class="abs h2" style="top:2934px;color:#fff;font-size:34px">Our Capabilites</h2>
  <div class="cap-tile dim" style="left:0;width:195px"><svg width="40" height="60" viewBox="0 0 40 60" fill="none" stroke="#555" stroke-width="2.5"><path d="M4 4h32v10H4zM14 14h12v18H14zM20 32v24"/></svg>Reaming</div>
  <div class="cap-tile" style="left:201px;width:195px"><svg width="56" height="60" viewBox="0 0 56 60" fill="none" stroke="#222" stroke-width="2.2"><path d="M6 4h44M18 4v14h20V4M24 18l4 10 4-10M28 30v8M4 46h48v8H4z"/></svg>Parting/Cutting</div>
  <div class="cap-tile" style="left:403px;width:193px"><svg width="60" height="60" viewBox="0 0 60 60" fill="none" stroke="#222" stroke-width="2.2"><circle cx="30" cy="30" r="16"/><circle cx="30" cy="30" r="4"/><path d="M10 10l16 16M4 52h52"/></svg>Facing</div>
  <div class="cap-tile" style="left:602px;width:195px"><svg width="60" height="60" viewBox="0 0 60 60" fill="none" stroke="#222" stroke-width="2.2"><path d="M22 4v30M16 34h12v8H16zM6 42h50v8H6zM36 34h14v8"/></svg>Turning</div>
  <div class="cap-tile" style="left:804px;width:194px"><svg width="60" height="60" viewBox="0 0 60 60" fill="none" stroke="#222" stroke-width="2.2"><path d="M10 54h40V40H10zM18 40V24l14-14 8 8-12 12v10"/><circle cx="40" cy="34" r="5"/></svg>Boring</div>
  <div class="cap-tile dim" style="left:1005px;width:195px"><svg width="60" height="60" viewBox="0 0 60 60" fill="none" stroke="#555" stroke-width="2.5"><path d="M18 4h24v12H18zM26 16h8v14h-8zM30 30v12M6 42h48v12H6z"/></svg>Drilling</div>
  <div class="arrow-box light" style="left:155px;top:3077px"><svg width="18" height="12" viewBox="0 0 18 12" fill="none" stroke="#fff" stroke-width="1.6"><path d="M17 6H1M6 1L1 6l5 5"/></svg></div>
  <div class="arrow-box light" style="left:1005px;top:3077px"><svg width="18" height="12" viewBox="0 0 18 12" fill="none" stroke="#fff" stroke-width="1.6"><path d="M1 6h16M12 1l5 5-5 5"/></svg></div>
  <div class="btn btn-light" style="left:533px;top:3233px;width:134px;height:40px">Contact Us</div>
  <svg class="abs" style="left:0;top:3310px" width="1200" height="115" viewBox="0 0 1200 115">
    <polygon points="0,0 1200,0 670,108 530,108" fill="var(--dark)"/>
    <polyline points="0,0 530,112 670,112 1200,0" fill="none" stroke="#3a3a3a" stroke-width="2"/>
  </svg>
</section>

<!-- contact -->
<section>
  <h2 class="abs h2" style="top:3470px">Contact Us</h2>
  <div class="abs" style="left:0;top:3803px;width:1200px;height:486px;background:var(--dark)"></div>
  <div class="abs" style="left:196px;top:3523px;width:801px;height:404px;background:#fff;box-shadow:0 4px 12px rgba(0,0,0,.15)"></div>
  <svg class="abs" style="left:196px;top:3523px" width="352" height="404" viewBox="0 0 352 404"><polygon points="0,0 170,0 350,404 0,404" fill="var(--panel)"/></svg>
  <div class="abs brand" style="left:230px;top:3625px;color:#fff">
    <span class="brand-mark" style="width:22px;height:22px"></span><span class="brand-name" style="font-size:14px">NORTHGATE CNC</span>
  </div>
  <div class="contact-item" style="top:3702px"><svg width="14" height="14" viewBox="0 0 24 24" fill="#fff"><path d="M5 3h4l2 5-3 2a11 11 0 0 0 6 6l2-3 5 2v4a2 2 0 0 1-2 2A17 17 0 0 1 3 5a2 2 0 0 1 2-2z"/></svg>(123) 456-7890</div>
  <div class="contact-item" style="top:3744px"><svg width="15" height="12" viewBox="0 0 24 18" fill="#fff"><path d="M0 0h24v18H0z"/><path d="M1 1l11 9 11-9" stroke="#2d2d2d" stroke-width="2" fill="none"/></svg>info@northgatecnc.com</div>
  <div class="contact-item" style="top:3790px"><svg width="14" height="18" viewBox="0 0 14 18" fill="#fff"><path d="M7 0a7 7 0 0 1 7 7c0 5-7 11-7 11S0 12 0 7a7 7 0 0 1 7-7z"/><circle cx="7" cy="7" r="2.5" fill="#2d2d2d"/></svg><span>123, Building Name, Street<br>City, State XY 123456</span></div>
  <div class="abs" style="left:230px;top:3863px;color:#fff;font-size:13px;text-decoration:underline">VIEW DIRECTIONS</div>

  <div class="field-label" style="left:516px;top:3590px;color:#333">First Name*</div>
  <div class="field-line" style="left:516px;top:3624px;width:213px;background:#555"></div>
  <div class="field-label" style="left:752px;top:3590px">Last Name*</div>
  <div class="field-line" style="left:752px;top:3624px;width:215px"></div>
  <div class="field-label" style="left:516px;top:3667px">Phone Number*</div>
  <div class="field-line" style="left:516px;top:3701px;width:213px"></div>
  <div class="field-label" style="left:752px;top:3667px">Postal Code*</div>
  <div class="field-line" style="left:752px;top:3701px;width:215px"></div>
  <div class="field-label" style="left:516px;top:3743px">Message*</div>
  <div class="field-line" style="left:516px;top:3777px;width:451px"></div>
  <div class="btn btn-dark" style="left:850px;top:3819px;width:99px;height:38px;font-size:14px">Submit</div>
</section>

<!-- footer -->
<footer>
  <div class="abs brand" style="left:0;top:4050px;width:1200px;justify-content:center;color:#fff">
    <span class="brand-mark" style="width:34px;height:34px"></span><span class="brand-name" style="font-size:22px;letter-spacing:3px">NORTHGATE CNC</span>
  </div>
  <span class="foot-nav" style="left:244px">Home</span>
  <span class="foot-nav" style="left:386px">About Us</span>
  <span class="foot-nav" style="left:550px">Services</span>
  <span class="foot-nav" style="left:707px">Capabilities</span>
  <span class="foot-nav" style="left:887px">Contact Us</span>
  <div class="abs" style="left:163px;top:4212px;width:876px;height:1px;background:#333"></div>
  <div class="abs" style="left:163px;top:4250px;font-size:13px;color:#ccc">© 2023 Northgate CNC. All Rights Reserved.</div>
  <div class="social" style="left:899px"></div>
  <div class="social" style="left:937px"></div>
  <div class="social" style="left:975px"></div>
  <div class="social" style="left:1013px"></div>
</footer>

</body>
</html>
```